Fall/Winter HVAC billboard

Looking to update our billboard for the heating season.
Want to $ave on heating bills
Consider it done!

Target Market(s)

Commuters - homeowners

Industry/Entity Type

HVAC - heating and Air conditioning

```html
<!DOCTYPE html>
<html lang="en">
<head>
<meta charset="utf-8">
<title>Brightvale Heating Season Billboard</title>
<link rel="stylesheet" href="https://fonts.googleapis.com/css2?family=Poppins:wght@400;600;700;800&display=swap">
<style>
  :root {
    --stage: #d6d6d6;
    --sunflower: #fbb61b;
    --ink: #0d0d0d;
    --sky: #29a8e0;
    --paper: #ffffff;
    --device-light: #f4f4f4;
    --device-shade: #c9c9c9;
  }
  * { box-sizing: border-box; margin: 0; padding: 0; }
  html, body {
    width: 1200px;
    height: 478px;
    overflow: hidden;
    background: var(--stage);
    font-family: "Poppins", sans-serif;
  }
  .billboard {
    position: absolute;
    left: 0;
    top: 60px;
    width: 1200px;
    height: 358px;
    background: var(--sunflower);
    overflow: hidden;
  }
  .hero-photo {
    position: absolute;
    left: 0;
    top: 0;
    width: 497px;
    height: 292px;
    background: radial-gradient(ellipse at 55% 45%, var(--device-light) 0%, #e6e6e6 45%, var(--device-shade) 70%, rgba(201,201,201,0) 100%);
  }
  .headline {
    position: absolute;
    left: 488px;
    top: 27px;
    color: var(--ink);
    font-weight: 800;
    text-transform: uppercase;
    letter-spacing: -1px;
  }
  .headline-line {
    display: block;
    font-size: 72px;
    line-height: 74px;
    white-space: nowrap;
  }
  .headline-highlight {
    display: inline-block;
    background: var(--sky);
    line-height: 71px;
    height: 71px;
    padding: 0 7px 0 4px;
  }
  .headline-close {
    display: block;
    font-size: 54px;
    line-height: 70px;
    white-space: nowrap;
    letter-spacing: -0.5px;
  }
  .contact-band {
    position: absolute;
    left: 0;
    bottom: 0;
    width: 1200px;
    height: 65px;
    background: var(--paper);
    display: flex;
    align-items: center;
    padding-left: 33px;
  }
  .contact-phone {
    display: flex;
    align-items: center;
    gap: 9px;
    font-size: 38px;
    font-weight: 700;
    color: var(--ink);
    letter-spacing: -0.5px;
    white-space: nowrap;
  }
  .phone-icon { width: 36px; height: 36px; }
  .contact-web {
    position: absolute;
    left: 494px;
    font-size: 25px;
    font-weight: 400;
    color: var(--ink);
    white-space: nowrap;
  }
  .contact-web strong { font-weight: 700; }
  .brand-tab {
    position: absolute;
    right: 0;
    bottom: 0;
    width: 422px;
    height: 101px;
    background: var(--paper);
    border-top-left-radius: 40px;
    display: flex;
    align-items: center;
    padding-left: 26px;
    gap: 10px;
  }
  .brand-mark {
    width: 48px;
    height: 48px;
    border-radius: 50%;
    background: var(--sky);
    flex: none;
  }
  .brand-name {
    font-size: 25px;
    font-weight: 800;
    color: var(--sky);
    letter-spacing: -0.3px;
    white-space: nowrap;
  }
  .brand-service {
    font-size: 12px;
    font-weight: 600;
    line-height: 15px;
    color: var(--sky);
    white-space: nowrap;
  }
</style>
</head>
<body>
  <section class="billboard">
    <div class="hero-photo" role="img" aria-label="Photo of a hand turning the dial of a white digital thermostat whose display reads SAVE"></div>

    <h1 class="headline">
      <span class="headline-line">Want to <span class="headline-highlight">$ave on</span></span>
      <span class="headline-line">Heating bills</span>
      <span class="headline-close">Consider it done!</span>
    </h1>

    <footer class="contact-band">
      <div class="contact-phone">
        <svg class="phone-icon" viewBox="0 0 38 38" aria-hidden="true">
          <circle cx="19" cy="19" r="18" fill="#29a8e0"/>
          <path d="M13.5 10.5c1-.6 2-.3 2.5.6l1.6 3c.4.8.2 1.7-.5 2.2l-1.2.9c.8 2 2.6 3.9 4.7 4.8l.9-1.2c.5-.7 1.5-.9 2.2-.5l3 1.6c.9.5 1.2 1.6.6 2.5l-1 1.6c-.6 1-1.8 1.5-2.9 1.1-5.3-1.6-9.4-5.7-11-11-.4-1.1.1-2.3 1.1-2.9z" fill="#ffffff"/>
        </svg>
        <span>Call 555-014-0199</span>
      </div>
      <div class="contact-web">www.<strong>brightvale</strong>.com</div>
    </footer>

    <div class="brand-tab">
      <span class="brand-mark"></span>
      <span class="brand-name">BRIGHTVALE</span>
      <span class="brand-service">Heating<br>&amp; Air Conditioning</span>
    </div>
  </section>
</body>
</html>
```